Pelbrook Metal Roofing INC.

Hello,
I am working with a local business to design them a new website. The designer I had worked with moved to colorado and has taken a new job. He recommended that I try posting my new jobs on here. I would need a design and assistance setting the site up on my host nimbus server. I work by myself and handle the sales side of things and need a designer that can help me out.
This company is a metal roofing business. The current page I made for them is www.pelbrookmetalinc.example

They would like the new site to be similar to http://www.tamblecreekalloy.example

Please let me know if this is something that you could do for us.
Updates

the company wants the site to look very similar to this http://www.tamblecreekalloy.exampleis that something you could do, please get in touch with me.Thanks Added Tuesday, January 10, 2017

Industry/Entity Type

Business

Font styles to use
Sans Serif

Colors
ed252d

Requirements
Must have
• the company wants the site to look very similar to this
• http://www.tamblecreekalloy.example
• is that something you could do, please get in touch with me.
• Thanks

```html
<!DOCTYPE html>
<html lang="en">
<head>
<meta charset="utf-8">
<title>Pelbrook Metal Inc</title>
<link href="https://fonts.googleapis.com/css2?family=Lato:wght@300;400;700;900&display=swap" rel="stylesheet">
<style>
:root{
  --red:#ed252d;
  --dark:#2b2b2b;
  --darker:#222;
  --text:#555;
  --light:#f4f4f4;
  --white:#fff;
}
*{box-sizing:border-box;margin:0;padding:0}
html,body{width:679px;height:1200px;overflow:hidden}
body{font-family:'Lato',sans-serif;color:var(--text);background:var(--white);position:relative}
.topbar{position:absolute;left:0;top:0;width:679px;height:64px;background:var(--dark)}
.logo{position:absolute;left:30px;top:8px;width:150px;height:40px;background:var(--red);color:var(--white);font-weight:700;font-size:13px;display:flex;align-items:center;justify-content:center;letter-spacing:.5px}
.phones{position:absolute;right:24px;top:14px;display:flex;gap:18px;color:var(--white);font-size:10px}
.phones span{display:flex;align-items:center;gap:5px}
.nav{position:absolute;left:0;top:64px;width:679px;height:30px;background:var(--white);display:flex;align-items:center;padding-left:92px;gap:4px}
.nav a{font-size:9px;font-weight:700;color:#333;text-decoration:none;padding:6px 10px;text-transform:uppercase}
.nav a.active{background:var(--red);color:var(--white)}
.nav .quote{margin-left:14px;background:var(--red);color:var(--white);padding:6px 12px}
.hero{position:absolute;left:0;top:94px;width:679px;height:336px;background:linear-gradient(180deg,#c9cfd6 0%,#b89870 45%,#8a6e52 100%)}
.hero-text{position:absolute;left:0;top:270px;width:679px;text-align:center}
.hero-text h1{color:var(--red);font-size:34px;font-weight:900;letter-spacing:1px;line-height:1}
.hero-text p{color:var(--white);font-size:17px;font-weight:700;margin-top:2px}
.section-title{font-size:18px;font-weight:700;color:#444;text-transform:uppercase;display:flex;align-items:center;gap:8px}
.section-title::before{content:"";width:4px;height:18px;background:var(--red)}
.featured{position:absolute;left:0;top:430px;width:679px;height:340px;background:var(--light);padding:30px 40px}
.cards{display:flex;gap:22px;margin-top:22px}
.card{width:185px;height:232px;background:var(--white);border-top:4px solid var(--red);padding:8px;text-align:center}
.card .ph{height:92px}
.card h3{font-size:12px;font-weight:700;color:#444;margin-top:14px;text-transform:uppercase;line-height:1.3}
.card p{font-size:7px;margin-top:6px;line-height:1.4}
.btn{display:inline-block;background:var(--red);color:var(--white);font-size:8px;font-weight:700;padding:6px 12px;margin-top:10px}
.btn.darkbtn{background:#333}
.info{position:absolute;left:0;top:770px;width:679px;height:235px;padding:30px 40px;display:flex;gap:40px}
.about{width:330px}
.about p{font-size:8px;line-height:1.6;margin-top:14px}
.downloads{width:230px}
.downloads ul{list-style:none;margin-top:12px}
.downloads li{font-size:8px;padding:4px 0;display:flex;gap:6px;align-items:center}
.downloads li::before{content:"";width:7px;height:8px;background:var(--red)}
.footer{position:absolute;left:0;top:1005px;width:679px;height:195px;background:var(--darker);padding:24px 40px;display:flex;gap:36px;color:#bbb}
.footer h4{color:var(--red);font-size:10px;font-weight:700;text-transform:uppercase;margin-bottom:12px}
.col{width:180px}
.proj{display:flex;gap:8px;margin-bottom:10px;font-size:7px;line-height:1.4}
.proj .th{width:38px;height:26px;flex:none;background:linear-gradient(135deg,#6b7e5a,#a98a62)}
.footer p{font-size:7px;line-height:1.5}
.input{margin-top:10px;height:20px;border:1px solid #555;background:#2f2f2f;font-size:7px;color:#888;padding:6px}
.contact .name{color:var(--white);font-size:12px;font-weight:700;margin-bottom:10px}
.contact .row{display:flex;gap:14px;font-size:8px;margin-bottom:10px}
.contact .hours{font-size:7px;line-height:1.6}
.contact strong{color:var(--white)}
</style>
</head>
<body>
<header class="topbar">
  <div class="logo">PELBROOK METAL INC</div>
  <div class="phones">
    <span><svg width="10" height="10" viewBox="0 0 10 10"><circle cx="5" cy="5" r="5" fill="#ed252d"/><path d="M3 2.5l1 1-0.6.8a4 4 0 002.3 2.3l.8-.6 1 1-.8.9A4.5 4.5 0 012.1 3.3z" fill="#fff"/></svg>555-201-0187</span>
    <span><svg width="10" height="10" viewBox="0 0 10 10"><circle cx="5" cy="5" r="5" fill="#ed252d"/><path d="M3 2.5l1 1-0.6.8a4 4 0 002.3 2.3l.8-.6 1 1-.8.9A4.5 4.5 0 012.1 3.3z" fill="#fff"/></svg>555-201-0452</span>
  </div>
</header>
<nav class="nav">
  <a class="active">Home</a><a>About Us</a><a>Products</a><a>Project Gallery</a><a>Contact</a><a class="quote">Get a Quote</a>
</nav>
<section class="hero" role="img" aria-label="Photo of a timber post frame building under construction">
  <div class="hero-text"><h1>MANUFACTURERS</h1><p>QUALITY BUILDING COMPONENTS</p></div>
</section>
<section class="featured">
  <h2 class="section-title">Featured Products</h2>
  <div class="cards">
    <div class="card"><div class="ph" role="img" aria-label="Photo of post frame trusses" style="background:linear-gradient(180deg,#cdb38a,#8f7450)"></div><h3>Complete Post Frame Building Packages</h3><p>Call us for a quote on your next post frame building project.</p><span class="btn">Call Us Now</span></div>
    <div class="card"><div class="ph" role="img" aria-label="Photo of a green metal roof" style="background:linear-gradient(180deg,#b8c7cf,#5f7a68)"></div><h3>Residential Metal Roofing</h3><p>Over 30 colour options and a range of lasting roofing profiles.</p><span class="btn">Call Us Now</span></div>
    <div class="card"><div class="ph" role="img" aria-label="Photo of a red agricultural barn" style="background:linear-gradient(180deg,#9fc0dc,#b0302f)"></div><h3>Commercial and Agricultural Applications</h3><p>All design needs met for farm and commercial projects.</p><span class="btn">Call Us Now</span></div>
  </div>
</section>
<section class="info">
  <div class="about">
    <h2 class="section-title">About Pelbrook</h2>
    <p>We are a family owned supplier of metal roofing and post frame building materials serving the region for many years. Our team cuts every panel to length and ships complete packages ready for your crew. We stock trim, fasteners, doors and lumber so each job comes together in one order. From small sheds to large commercial barns, we help customers plan, price and build with confidence and lasting quality.</p>
    <span class="btn darkbtn">Click Here To Know More</span>
  </div>
  <div class="downloads">
    <h2 class="section-title">Downloads</h2>
    <ul><li>New Product Catalog &amp; Trim Details</li><li>Old Product Catalog</li><li>Corner Brace Brochure</li><li>Color Chart</li><li>Panel Coating Warranty</li></ul>
    <span class="btn darkbtn">View All</span>
  </div>
</section>
<footer class="footer">
  <div class="col">
    <h4>Recent Projects</h4>
    <div class="proj"><div class="th" role="img" aria-label="Project photo"></div><span>New machine shed finished with steel roof panels</span></div>
    <div class="proj"><div class="th" role="img" aria-label="Project photo"></div><span>Red horse barn built from full post frame kit</span></div>
    <div class="proj"><div class="th" role="img" aria-label="Project photo"></div><span>Home reroof with standing seam panels in grey</span></div>
  </div>
  <div class="col">
    <h4>Newsletter Signup</h4>
    <p>Sign up for news on products, seasonal pricing and project ideas from our team.</p>
    <div class="input">Your email address</div>
    <span class="btn">Subscribe</span>
  </div>
  <div class="col contact">
    <h4>Contact Info</h4>
    <div class="name">PELBROOK METAL INC</div>
    <div class="row"><span>555-201-0187</span><span>555-201-0452</span></div>
    <div class="hours"><strong>Working Hours</strong><br>Monday - Friday: 7am - 5pm<br>Saturday: 7am - 12pm &nbsp; Sunday: Closed</div>
  </div>
</footer>
</body>
</html>
```